Web site - 5-8 page

We are a small, fresh pasta business called The Noodle Lark located in suburbs of Sacramento, CA. We sell our pasta, ravioli, meatballs and sauce at farmer's markets, events, and soon in our café & marketplace. (Jan 2014) . We also provide catering services. The site needs to communicate FRESH, local, no preservatives, artisan quality pasta. We offer vegetarian, vegan and gluten free products as well.

We would like a web site using our logos and colors to feature what we do, and where people can come buy it. A page to our standard take and make items/menu, our seasonal take and make menu, our catering menu, our new hot food café menu.

We want a page that we can update with "Where can you find The Noodle Lark"
A "specials page" and a page they can order from that they choose the location to pick it up or in the delivery area we deliver to them.
A page with photo's and referrals, testimony, comments, about us, etc. Maybe a page for recipes.
We need to update the events/find us page all the time, weekly, so it needs to be easy for us to go in and do that. We are Window's (not MAC) users if that makes a difference or not, not sure.

Ideally, the same person(s) that make the website would also do a separate project creating our catering and hot food menu brochure/layout and recipe cards

Reason: allow enough time for good quality work

I would like to see the landing page have the pasta shapes/sizes element that is found in the refrigerator wrap, the wrap on the trailer, and the menu - see photo and uploads. It's used as a banner or as a background, bright green.

                                   

 

Would like visitors to be able to "like" me or follow me from my web page. A button or a link?

                                        http://www.brightpantry-example.com/our-food/

Really like the layout of this site. More grocery oriented than café, but we are a take and make marketplace as well as a Panini salads and hot pasta menu for lunch.

Please add Café + Marketplace to headers. Our logo is good but we are now adding a café element and a fresh marketplace, se we need to communicate what we are/what we do. We think adding Café + Marketplace as a descriptor will help. Any ideas, feel free to put your own spin on it. Thank you!!

The designs are good...thanks to everyone!

Reason: To allow for the many updates we have added. Good designs coming in, thank you!

Target Market(s)

#1, busy mom's, busy family's (FAST, Economical meals, no preservatives, local food)
#2 24-34 yr olds that want fresh, vegetarian, vegan or gluten free meal options (no preservatives, local food)
#3 Fresh pasta lovers - any age. The enjoyment of quality fresh pasta and a good meal experience sharing it with friends and family

Industry/Entity Type

Catering

Font styles to use
Other font styles liked:
• EideticNeoRegular, duffy

Colors
9bcb3c
f78f20
eb1f27

Requirements
Must have
• Address, phone, name, logo, colors
Fresh pasta, ravioli, sauce and meatballs in take and make convenient packages. Stress fresh, preservative free, local ingredients, cooks in 45 SECONDS to 3.5 minutes depending on the pasta cut.
FAST meal
Where to find us page - upcoming events
A "specials" page
A page for recipe, how to cook our pasta, how to freeze and store fresh pasta,
How to order online page
Nice to have
• Testimony, links to Facebook, twitter, etc. Place for photo's of product, recent events, customer comments on how they used the product to create their recipe.
Should not have
• No stock photo's of tomato's, no dried pasta images, no Italian flags. No cheesy old world Italian loo or feel. Think fresh, modern, FAST!

```html
<!DOCTYPE html>
<html lang="en">
<head>
<meta charset="utf-8">
<title>The Noodle Lark – Recent Recipe List View</title>
<link rel="stylesheet" href="https://fonts.googleapis.com/css2?family=Ribeye&family=Alegreya:ital,wght@0,400;0,700;1,700&family=Arimo:wght@400;700&display=swap">
<style>
:root{
  --page:#f1f1ee;
  --green:#8dc21f;
  --green-dark:#5a8a12;
  --green-deep:#3f7a0c;
  --title-green:#4e8a10;
  --red:#e8262b;
  --orange:#f7a21b;
  --text:#444;
  --muted:#888;
  --card:#ffffff;
  --line:#cfcfcf;
  --star:#f5b400;
  --star-off:#9b9b9b;
}
*{box-sizing:border-box;margin:0;padding:0}
html,body{width:1015px;height:1200px;overflow:hidden}
body{background:var(--page);font-family:"Alegreya",Georgia,serif;color:var(--text);position:relative}
.abs{position:absolute}
.top-band{left:0;top:0;width:1015px;height:47px;background:linear-gradient(var(--green-dark),var(--green) 55%,var(--green-dark))}
.brand{left:141px;top:60px;width:100px;text-align:center}
.brand-mark{width:62px;height:62px;border-radius:50%;background:var(--red);margin:0 auto 6px}
.brand-name{font-family:"Alegreya",serif;font-weight:700;font-size:15px;color:var(--red);line-height:1.1}
.nav{left:440px;top:78px;display:flex;gap:0}
.nav a{display:block;text-decoration:none;font-family:"Ribeye",serif;font-size:15px;color:var(--title-green);width:84px;text-align:center;line-height:1.05}
.nav a small{display:block;font-family:"Alegreya",serif;font-size:10px;color:var(--muted)}
.nav .active{position:absolute;left:373px;top:-7px;width:67px;height:43px;background:var(--green-deep);color:#fff;padding-top:7px}
.nav .active small{color:#dfe9cc}
.page-title{left:152px;top:166px;font-family:"Ribeye",serif;font-size:23px;color:var(--red);font-weight:400}
.rule{border-top:1px dashed #aaa}
.card{left:163px;width:457px;height:150px;background:var(--card);box-shadow:0 2px 4px rgba(0,0,0,.18);border-bottom:3px solid #e3e3e3}
.card .photo{position:absolute;left:5px;top:5px;width:207px;height:140px}
.card h2{position:absolute;left:222px;top:7px;font-family:"Ribeye",serif;font-weight:400;font-size:14px;color:var(--title-green)}
.card p{position:absolute;left:222px;top:25px;width:228px;font-size:12.6px;line-height:16px;color:#555}
.card .stars{position:absolute;left:222px;top:104px}
.card .more{position:absolute;right:9px;top:123px;font-weight:700;font-size:11px;color:var(--red);text-decoration:none}
.stars{display:flex;gap:5px}
.stars svg{width:17px;height:17px}
.pager{left:160px;top:939px;font-size:11px;display:flex;align-items:center;gap:11px;color:#555}
.pager .cur{width:11px;height:11px;background:var(--green-deep);display:inline-block}
.side h3{font-family:"Ribeye",serif;font-weight:400;font-size:15px;color:var(--title-green)}
.search{left:660px;top:261px;width:194px;height:24px;background:#fff;border:1px solid #ddd;font-size:9px;color:#777;padding:6px 4px}
.search svg{position:absolute;right:4px;top:3px}
.archives{left:660px;top:347px;width:195px;list-style:none}
.archives li{height:28.3px;border-bottom:1px dashed #ccc;font-size:10.5px;color:#555;display:flex;align-items:center;gap:11px}
.tabs{left:662px;top:578px;display:flex;gap:2px}
.tabs span{font-size:10px;padding:5px 6px;border:1px solid #ccc;border-bottom:none;background:#e8e8e6;color:#555}
.tabs span.on{background:#fff;color:var(--title-green)}
.fav{left:662px;top:601px;width:193px;height:294px;background:#fff;border:1px solid #ddd;box-shadow:0 2px 3px rgba(0,0,0,.1)}
.fav-item{position:absolute;left:8px;width:180px}
.fav-item .thumb{position:absolute;left:0;top:0;width:51px;height:51px;border:2px solid #fff;box-shadow:0 0 0 1px #ccc}
.fav-item .txt{position:absolute;left:61px;top:-6px;width:120px;font-size:12px;line-height:16px}
.fav-item .txt b{font-weight:400;color:var(--green-dark)}
.fav-item .meta{display:block;font-size:9.5px;color:var(--green-dark)}
.fav-item .stars{gap:3px;margin-top:2px}
.fav-item .stars svg{width:15px;height:15px}
.footer{left:0;top:981px;width:1015px;height:188px;background:var(--green)}
.footer-base{left:0;top:1169px;width:1015px;height:31px;background:var(--green-deep);color:#e9f2da;font-family:"Arimo",sans-serif;font-size:8.5px;text-align:center;padding-top:11px}
.map{left:152px;top:1000px;width:124px;height:120px;border:3px solid #fff;background:linear-gradient(135deg,#ecebe6,#d9d7cf)}
.contact{left:293px;top:1002px;font-family:"Arimo",sans-serif;font-size:8.5px;color:#fff;line-height:15px}
.contact strong{display:block;margin-bottom:6px}
.contact p{margin-bottom:6px}
.btn{left:292px;top:1102px;width:68px;height:20px;background:var(--red);color:#fff;font-family:"Arimo",sans-serif;font-size:9.5px;text-align:center;line-height:20px;border-radius:2px}
.vdivider{left:500px;top:998px;height:138px;border-left:2px dashed #6a9e16}
.dish{width:86px;height:86px;border-radius:50%;border:3px solid #fff}
.tag{left:500px;width:515px;text-align:center;font-family:"Alegreya",serif;font-style:italic;font-weight:700;color:#fff}
</style>
</head>
<body>
<svg width="0" height="0" style="position:absolute">
  <defs>
    <symbol id="star" viewBox="0 0 24 24"><path d="M12 1.8l3 6.4 7 .8-5.2 4.8 1.4 7-6.2-3.6-6.2 3.6 1.4-7L2 9l7-.8z" stroke="#fff" stroke-width="1"/></symbol>
    <symbol id="cal" viewBox="0 0 12 12"><rect x="1" y="2" width="10" height="9" fill="#fff" stroke="#7aa93a"/><rect x="1" y="2" width="10" height="2.5" fill="#7aa93a"/><path d="M3 6.5h6M3 8.5h6" stroke="#9bc35a"/></symbol>
  </defs>
</svg>

<header>
  <div class="abs top-band"></div>
  <div class="abs brand"><div class="brand-mark"></div><div class="brand-name">The Noodle Lark</div></div>
  <nav class="abs nav">
    <a href="#">Home<small>Home Page</small></a>
    <a href="#">Events<small>Events Page</small></a>
    <a href="#">Specials<small>Specials Page</small></a>
    <a href="#">Gallery<small>Gallery Page</small></a>
    <a href="#" class="active">Recipes<small>Recipes Page</small></a>
  </nav>
</header>

<main>
  <h1 class="abs page-title">Recent Recipe List View</h1>
  <div class="abs rule" style="left:152px;top:202px;width:702px"></div>

  <article class="abs card" style="top:224px">
    <div class="photo" role="img" aria-label="Photo of fresh vegetables with broccoli, carrot and dip" style="background:linear-gradient(120deg,#e9d9a8,#5b9a2a 45%,#e0672a)"></div>
    <h2>Recipe title will appear</h2>
    <p>Lorem ipsum dolor sit amet, consectetuer adipiscing elit, sed diam nonummy nibh euis-mod tincidunt ut laoreet dolore magna aliquam erat volutpat. Ut wisi enim ad minim veniam,</p>
    <div class="stars"><svg fill="var(--star)"><use href="#star"/></svg><svg fill="var(--star)"><use href="#star"/></svg><svg fill="var(--star)"><use href="#star"/></svg><svg fill="var(--star)"><use href="#star"/></svg><svg fill="var(--star-off)"><use href="#star"/></svg></div>
    <a class="more" href="#">Read more »</a>
  </article>

  <article class="abs card" style="top:400px">
    <div class="photo" role="img" aria-label="Photo of pasta salad with greens and olives" style="background:linear-gradient(130deg,#9fbf4a,#d9c873 50%,#6f8f2c)"></div>
    <h2>Recipe title will appear</h2>
    <p>Lorem ipsum dolor sit amet, consectetuer adipiscing elit, sed diam nonummy nibh euis-mod tincidunt ut laoreet dolore magna aliquam erat volutpat. Ut wisi enim ad minim veniam,</p>
    <div class="stars"><svg fill="var(--star)"><use href="#star"/></svg><svg fill="var(--star)"><use href="#star"/></svg><svg fill="var(--star)"><use href="#star"/></svg><svg fill="var(--star)"><use href="#star"/></svg><svg fill="var(--star-off)"><use href="#star"/></svg></div>
    <a class="more" href="#">Read more »</a>
  </article>

  <article class="abs card" style="top:579px">
    <div class="photo" role="img" aria-label="Photo of spaghetti with basil and red pepper" style="background:linear-gradient(140deg,#e7ddc4,#f1d97a 50%,#c98a3a)"></div>
    <h2>Recipe title will appear</h2>
    <p>Lorem ipsum dolor sit amet, consectetuer adipiscing elit, sed diam nonummy nibh euis-mod tincidunt ut laoreet dolore magna aliquam erat volutpat. Ut wisi enim ad minim veniam,</p>
    <div class="stars"><svg fill="var(--star)"><use href="#star"/></svg><svg fill="var(--star)"><use href="#star"/></svg><svg fill="var(--star)"><use href="#star"/></svg><svg fill="var(--star)"><use href="#star"/></svg><svg fill="var(--star-off)"><use href="#star"/></svg></div>
    <a class="more" href="#">Read more »</a>
  </article>

  <article class="abs card" style="top:757px">
    <div class="photo" role="img" aria-label="Photo of penne with green beans and herbs" style="background:linear-gradient(130deg,#49502e,#c8c58a 50%,#6b8a3a)"></div>
    <h2>Recipe title will appear</h2>
    <p>Lorem ipsum dolor sit amet, consectetuer adipiscing elit, sed diam nonummy nibh euis-mod tincidunt ut laoreet dolore magna aliquam erat volutpat. Ut wisi enim ad minim veniam,</p>
    <div class="stars"><svg fill="var(--star)"><use href="#star"/></svg><svg fill="var(--star)"><use href="#star"/></svg><svg fill="var(--star)"><use href="#star"/></svg><svg fill="var(--star)"><use href="#star"/></svg><svg fill="var(--star-off)"><use href="#star"/></svg></div>
    <a class="more" href="#">Read more »</a>
  </article>

  <div class="abs rule" style="left:152px;top:931px;width:478px"></div>
  <div class="abs pager">
    <svg width="10" height="8" viewBox="0 0 10 8"><path d="M9 4H1M4 1L1 4l3 3" stroke="#555" fill="none"/></svg><span>Next</span><span>1</span><span class="cur"></span><span>3</span><span>4</span><span>Previous</span><svg width="10" height="8" viewBox="0 0 10 8"><path d="M1 4h8M6 1l3 3-3 3" stroke="#555" fill="none"/></svg>
  </div>

  <aside class="side">
    <h3 class="abs" style="left:663px;top:231px">Search</h3>
    <div class="abs search">To search type and hit enter
      <svg width="18" height="18" viewBox="0 0 18 18"><circle cx="7" cy="7" r="5" stroke="#555" stroke-width="2" fill="none"/><path d="M11 11l5 5" stroke="#555" stroke-width="3"/></svg>
    </div>
    <h3 class="abs" style="left:663px;top:314px">Archives</h3>
    <ul class="abs archives">
      <li><svg width="12" height="12"><use href="#cal"/></svg>February 2014</li>
      <li><svg width="12" height="12"><use href="#cal"/></svg>January 2014</li>
      <li><svg width="12" height="12"><use href="#cal"/></svg>December 2013</li>
      <li><svg width="12" height="12"><use href="#cal"/></svg>November 2013</li>
      <li><svg width="12" height="12"><use href="#cal"/></svg>August 2013</li>
      <li><svg width="12" height="12"><use href="#cal"/></svg>July 2013</li>
    </ul>
    <h3 class="abs" style="left:661px;top:544px">Favourite Recipes</h3>
    <div class="abs tabs"><span class="on">Popular</span><span>Recents</span><span>Random</span></div>
    <div class="abs fav">
      <div class="fav-item" style="top:22px">
        <div class="thumb" role="img" aria-label="Thumbnail of a pasta dish" style="background:linear-gradient(135deg,#7f8a3a,#d7c98a)"></div>
        <div class="txt"><b>Lorem Ipsum has</b> been the industry..........<span class="meta">Nov 5, 2013 - 3 Comments</span>
          <div class="stars"><svg fill="var(--star)"><use href="#star"/></svg><svg fill="var(--star)"><use href="#star"/></svg><svg fill="var(--star)"><use href="#star"/></svg><svg fill="var(--star)"><use href="#star"/></svg><svg fill="var(--star-off)"><use href="#star"/></svg></div></div>
      </div>
      <div class="fav-item" style="top:111px">
        <div class="thumb" role="img" aria-label="Thumbnail of a pasta salad" style="background:linear-gradient(135deg,#9fbf4a,#d9c873)"></div>
        <div class="txt"><b>Lorem Ipsum has</b> been the industry..........<span class="meta">Nov 5, 2013 - 3 Comments</span>
          <div class="stars"><svg fill="var(--star)"><use href="#star"/></svg><svg fill="var(--star)"><use href="#star"/></svg><svg fill="var(--star)"><use href="#star"/></svg><svg fill="var(--star)"><use href="#star"/></svg><svg fill="var(--star-off)"><use href="#star"/></svg></div></div>
      </div>
      <div class="fav-item" style="top:202px">
        <div class="thumb" role="img" aria-label="Thumbnail of spaghetti with tomato" style="background:linear-gradient(135deg,#f0e2c0,#d6733a)"></div>
        <div class="txt"><b>Lorem Ipsum has</b> been the industry..........<span class="meta">Nov 5, 2013 - 3 Comments</span>
          <div class="stars"><svg fill="var(--star)"><use href="#star"/></svg><svg fill="var(--star)"><use href="#star"/></svg><svg fill="var(--star)"><use href="#star"/></svg><svg fill="var(--star)"><use href="#star"/></svg><svg fill="var(--star-off)"><use href="#star"/></svg></div></div>
      </div>
    </div>
  </aside>
</main>

<footer>
  <div class="abs footer"></div>
  <div class="abs map" role="img" aria-label="Street map showing the shop location"></div>
  <div class="abs contact">
    <strong>The Noodle Lark:</strong>
    <p>8:00 am - 4:00pm</p>
    <p>42 Alder Rd. Elk Grove<br>USA<br>Phone: 081-555-0142</p>
  </div>
  <div class="abs btn">Contact us ▸</div>
  <div class="abs vdivider"></div>
  <div class="abs dish" role="img" aria-label="Round photo of penne pasta" style="left:531px;top:1003px;background:linear-gradient(135deg,#e6c36b,#8a5a2a)"></div>
  <div class="abs dish" role="img" aria-label="Round photo of pasta salad" style="left:647px;top:1003px;background:linear-gradient(135deg,#c8553a,#7fa03a)"></div>
  <div class="abs dish" role="img" aria-label="Round photo of spaghetti with tomato sauce" style="left:758px;top:1003px;background:linear-gradient(135deg,#f2e6c8,#d35a32)"></div>
  <div class="abs tag" style="top:1106px;font-size:14px">We ove Pastas !!</div>
  <div class="abs tag" style="top:1128px;font-size:13px">www.thenoodlelark.com</div>
  <div class="abs footer-base">© 2013 by The Noodle Lark. All right reserved.</div>
</footer>
</body>
</html>
```